Motorcycle Shop Business Card

New business card for Motorcycle repair and customization shop.Business name: Steel Falcon Chris Morris443-865-5190, 2817 Harbor Lane Arbutus, MD 21094. www.dana@steelfalconcycles.example. I uploaded some motorcycle images and logo and a couple of our calendar shoots. They do not have to be used on card just examples of some of our work and past graphic work.
We work on Kestrel Brandt and Custom Built Motorcycles.

Looking for front and back design

Motorcycle owners

```html
<!DOCTYPE html>
<html lang="en">
<head>
<meta charset="UTF-8">
<title>Steel Falcon Customs — Business Card</title>
<link href="https://fonts.googleapis.com/css2?family=Exo+2:wght@400;600;800&display=swap" rel="stylesheet">
<style>
  :root {
    --page: #e6e6e6;
    --card-light: #eef0f2;
    --red: #c8102e;
    --red-deep: #a50d24;
    --red-bright: #e0162f;
    --ink: #111111;
    --ink-soft: #222222;
    --icon-bar: #b9b9b9;
    --tile-white: #ffffff;
  }
  * { margin: 0; padding: 0; box-sizing: border-box; }
  html, body {
    width: 1200px; height: 1200px; overflow: hidden;
    background: var(--page);
    font-family: "Exo 2", Arial, sans-serif;
  }
  .canvas { position: relative; width: 1200px; height: 1200px; }
  .card {
    position: absolute; left: 220px; width: 760px; height: 434px;
    box-shadow: 0 6px 18px rgba(0,0,0,0.18);
    overflow: hidden;
  }

  /* Back side: gallery of work */
  .card-back { top: 100px; background: var(--red); padding: 26px; }
  .gallery {
    display: grid;
    grid-template-columns: repeat(3, 1fr);
    grid-template-rows: repeat(2, 1fr);
    gap: 8px;
    width: 100%; height: 100%;
  }
  .tile { width: 100%; height: 100%; }
  .tile-bike-teal { background: radial-gradient(ellipse at 50% 60%, #b7c7cc 0%, #e8eef0 45%, var(--tile-white) 75%); }
  .tile-winged-scene { background: radial-gradient(ellipse at 50% 45%, #8a7a6a 0%, #2d3f52 45%, #141d2a 100%); }
  .tile-bike-red { background: radial-gradient(ellipse at 50% 60%, #9a9a9a 0%, #e2e2e2 45%, var(--tile-white) 75%); }
  .tile-garage-shoot { background: radial-gradient(ellipse at 45% 45%, #8a8a8a 0%, #3c3c3c 55%, #161616 100%); }
  .tile-bike-blue { background: radial-gradient(ellipse at 50% 60%, #5a6fb0 0%, #d7dcea 45%, var(--tile-white) 75%); }
  .tile-neon-shoot { background: radial-gradient(ellipse at 50% 55%, #f2f2f2 0%, #9a9a9a 55%, #6e6e6e 100%); }

  /* Front side: contact details */
  .card-front { top: 650px; background: var(--card-light); }
  .wave { position: absolute; left: 0; bottom: 0; width: 760px; height: 434px; }
  .brand {
    position: absolute; left: 56px; top: 160px;
    display: flex; align-items: center; gap: 12px;
  }
  .brand-dot {
    width: 34px; height: 34px; border-radius: 50%;
    background: var(--ink);
  }
  .brand-name {
    font-weight: 800; font-size: 28px; line-height: 1.05;
    color: var(--ink); text-transform: uppercase; letter-spacing: 1px;
  }
  .contact { position: absolute; left: 366px; top: 60px; }
  .person-name {
    font-weight: 800; font-size: 38px; color: var(--ink);
    text-transform: uppercase; letter-spacing: 0.5px;
    margin-bottom: 14px;
  }
  .details { display: flex; gap: 14px; }
  .icon-bar {
    width: 36px; background: var(--icon-bar);
    display: flex; flex-direction: column; align-items: center;
    justify-content: space-around; padding: 8px 0;
  }
  .icon-bar svg { width: 18px; height: 18px; }
  .detail-list { list-style: none; }
  .detail-list li {
    font-size: 17px; font-weight: 400; color: var(--ink-soft);
    line-height: 26px;
  }
  .detail-list .address {
    font-size: 15px; line-height: 20px; text-transform: uppercase;
    margin-top: 4px;
  }
</style>
</head>
<body>
<main class="canvas">

  <section class="card card-back" aria-label="Card back">
    <div class="gallery">
      <div class="tile tile-bike-teal" role="img" aria-label="Custom chopper with teal and white paint on a white background"></div>
      <div class="tile tile-winged-scene" role="img" aria-label="Illustration of a winged figure against a dark stormy sky"></div>
      <div class="tile tile-bike-red" role="img" aria-label="Black and red custom motorcycle on a white background"></div>
      <div class="tile tile-garage-shoot" role="img" aria-label="Black and white calendar photo in a garage full of motorcycles"></div>
      <div class="tile tile-bike-blue" role="img" aria-label="Blue custom chopper with chrome wheels on a white background"></div>
      <div class="tile tile-neon-shoot" role="img" aria-label="Calendar shoot with a custom motorcycle and neon script on grey"></div>
    </div>
  </section>

  <section class="card card-front" aria-label="Card front">
    <svg class="wave" viewBox="0 0 760 434" preserveAspectRatio="none" aria-hidden="true">
      <path d="M0 434 L0 360 C120 300 230 330 360 330 C520 330 640 250 760 150 L760 434 Z" fill="var(--red-deep)"/>
      <path d="M0 434 L0 380 C140 320 260 345 390 340 C540 335 660 260 760 180 L760 434 Z" fill="var(--red)"/>
      <path d="M0 434 L0 410 C180 360 330 380 470 370 C600 360 690 300 760 240 L760 434 Z" fill="var(--red-bright)"/>
    </svg>

    <div class="brand">
      <span class="brand-dot" aria-hidden="true"></span>
      <span class="brand-name">Steel Falcon<br>Customs</span>
    </div>

    <div class="contact">
      <h1 class="person-name">Dana Whitlock</h1>
      <div class="details">
        <div class="icon-bar" aria-hidden="true">
          <svg viewBox="0 0 24 24"><path d="M6.6 10.8a15 15 0 006.6 6.6l2.2-2.2a1 1 0 011-.25 11.4 11.4 0 003.6.6 1 1 0 011 1V20a1 1 0 01-1 1A17 17 0 013 4a1 1 0 011-1h3.5a1 1 0 011 1 11.4 11.4 0 00.6 3.6 1 1 0 01-.25 1z" fill="#fff"/></svg>
          <svg viewBox="0 0 24 24"><rect x="2" y="5" width="20" height="14" rx="1" fill="#fff"/><path d="M2 6l10 7 10-7" stroke="#b9b9b9" stroke-width="2" fill="none"/></svg>
          <svg viewBox="0 0 24 24"><circle cx="12" cy="12" r="9" fill="none" stroke="#fff" stroke-width="2"/><path d="M3 12h18M12 3c3 3 3 15 0 18M12 3c-3 3-3 15 0 18" stroke="#fff" stroke-width="1.5" fill="none"/></svg>
          <svg viewBox="0 0 24 24"><path d="M12 2a7 7 0 00-7 7c0 5 7 13 7 13s7-8 7-13a7 7 0 00-7-7z" fill="#fff"/><circle cx="12" cy="9" r="2.5" fill="#b9b9b9"/></svg>
        </div>
        <ul class="detail-list">
          <li>410-372-6814</li>
          <li>dana@steelfalconcycles.example</li>
          <li>www.steelfalconcycles.example</li>
          <li class="address">2817 Harbor Lane Elmhaven,<br>NR 21094.</li>
        </ul>
      </div>
    </div>
  </section>

</main>
</body>
</html>
```